Medical Staffing Pamphlet

We are starting to staff for Medical positions for the first time, we need pamphlets to take to medical facilities to try to gain new business

Need an copy to edit, many errors.

```html
<!DOCTYPE html>
<html lang="en">
<head>
<meta charset="utf-8">
<title>Crestline Staffing Medical – Trifold Brochure</title>
<link href="https://fonts.googleapis.com/css2?family=Oswald:wght@500;600&family=Open+Sans:wght@400;600;700&display=swap" rel="stylesheet">
<style>
:root{
  --stage:#e5e5e4;
  --navy:#1d3a78;
  --navy-deep:#11275a;
  --sky:#1f8fd1;
  --sky-soft:#49a9e0;
  --green:#8cc63f;
  --lime:#b5d334;
  --paper:#ffffff;
  --panel-grey:#f0f0ee;
  --ink:#3c4250;
  --ink-soft:#6b7080;
}
*{box-sizing:border-box;margin:0;padding:0}
html,body{width:1200px;height:2402px;overflow:hidden}
body{background:var(--stage);font-family:"Open Sans",Arial,sans-serif;color:var(--ink)}
.stage{height:800px;display:flex;align-items:center;justify-content:center}
.stage:first-child{height:802px}
.spread{width:1000px;height:773px;display:grid;grid-template-columns:repeat(3,1fr);box-shadow:0 10px 30px rgba(0,0,0,.18)}
.single{width:334px;height:773px;box-shadow:0 10px 30px rgba(0,0,0,.18)}
.panel{position:relative;overflow:hidden;height:773px}
.heading{font-family:"Oswald",Arial,sans-serif;font-weight:600;text-transform:uppercase;letter-spacing:.5px}
.footer-bar{position:absolute;left:0;right:0;bottom:0;height:32px;background:var(--green);color:#fff;font-size:10px;font-weight:700;letter-spacing:2px;text-transform:uppercase;display:flex;align-items:center;justify-content:center}
.photo{position:absolute;left:0;right:0}

/* cover */
.cover{background:var(--paper)}
.brand{position:absolute;top:34px;left:0;right:0;display:flex;align-items:center;justify-content:center;gap:12px}
.brand-square{width:40px;height:40px;background:var(--navy)}
.brand-name{font-family:"Oswald",Arial,sans-serif;font-weight:600;color:var(--navy);font-size:26px;line-height:1;text-transform:uppercase}
.cover .photo{top:128px;height:330px;background:linear-gradient(160deg,#eef3f7 0%,#cfdfe9 45%,#7fc3e3 75%,#e9eef2 100%)}
.cover-band{position:absolute;left:0;right:0;top:380px;width:334px;height:393px}
.cover-copy{position:absolute;left:34px;right:26px;top:540px}
.cover-kicker{color:var(--lime);font-size:24px}
.cover-title{color:#fff;font-weight:600;font-size:24px;line-height:1.25;margin-top:10px;text-transform:uppercase}

/* outside flap */
.flap{background:var(--panel-grey)}
.flap .photo{top:0;height:215px;background:linear-gradient(135deg,#d9d6e6 0%,#b9b4d1 40%,#e7e7ee 70%,#c9d3de 100%)}
.flap-body{position:absolute;top:240px;left:30px;right:26px}
.flap-heading{color:var(--navy);font-size:16px;line-height:1.3}
.flap-text{font-size:10.5px;line-height:1.65;color:var(--ink-soft);margin-top:14px}
.flap-sub{color:var(--navy);font-size:11px;margin-top:22px}
.tick-list{list-style:none;margin-top:10px}
.tick-list li{display:flex;align-items:center;gap:8px;font-size:10.5px;line-height:2;color:var(--ink-soft)}
.tick{width:11px;height:11px;flex:none}

/* back panel */
.back{background:linear-gradient(180deg,var(--navy-deep) 0%,var(--navy) 70%)}
.back-mark{position:absolute;top:46px;left:50%;margin-left:-52px;width:104px;height:104px;background:#fff}
.back-body{position:absolute;top:178px;left:30px;right:30px;text-align:center;color:#fff}
.back-kicker{color:var(--lime);font-size:20px}
.back-text{font-size:11px;line-height:1.6;margin-top:10px;color:#dfe6f2}
.contact-title{color:var(--lime);font-size:20px;margin-top:36px}
.contact-rule{width:120px;height:1px;background:var(--lime);margin:6px auto 12px}
.contact-lines{font-size:13px;line-height:1.55}
.social{display:flex;justify-content:center;gap:10px;margin-top:16px}
.social span{width:18px;height:18px;border-radius:50%;border:1px solid #fff}
.back-wave{position:absolute;left:0;bottom:0;width:334px;height:220px}

/* inside */
.team-photo{position:absolute;top:0;left:0;width:667px;height:235px;background:linear-gradient(120deg,#a9d3ee 0%,#f4f7fa 30%,#dbe9f3 55%,#5da8d9 75%,#eef3f7 100%)}
.inside-left{background:var(--panel-grey)}
.inside-left-curve{position:absolute;top:205px;left:0;width:334px;height:60px}
.about{position:absolute;top:300px;left:32px;right:30px;text-align:center}
.about-heading{color:var(--navy);font-size:18px}
.about-rule{width:80px;height:2px;background:var(--green);margin:8px auto 16px}
.about-text{font-size:11px;line-height:1.75;color:var(--ink-soft);text-align:justify}
.about-pledge{color:var(--navy);font-size:17px;line-height:1.35;margin-top:34px}
.inside-mid{background:var(--paper)}
.inside-mid-curve{position:absolute;top:205px;left:0;width:333px;height:60px}
.services{position:absolute;top:262px;left:18px;right:20px;list-style:none}
.service{display:flex;gap:12px;margin-bottom:18px}
.service-icon{width:44px;height:44px;flex:none;border-radius:50%;background:#e2f1fa;display:flex;align-items:center;justify-content:center}
.service-title{color:var(--navy);font-size:13px}
.service-text{font-size:9.5px;line-height:1.55;color:var(--ink-soft);margin-top:2px}
.inside-right{background:linear-gradient(180deg,var(--navy) 0%,var(--navy-deep) 100%)}
.offer{position:absolute;top:42px;left:34px;right:28px;color:#fff}
.offer-heading{font-size:22px;text-align:center}
.offer-rule{width:100px;height:1px;background:#fff;margin:6px auto 0}
.offer-group{color:var(--lime);font-size:15px;text-align:center;margin-top:20px;font-family:"Oswald",Arial,sans-serif;font-weight:500;text-transform:uppercase}
.offer-list{list-style:none;margin-top:10px}
.offer-list li{display:flex;align-items:center;gap:9px;font-size:12px;line-height:2.05}
.inside-right .photo{top:520px;height:221px;background:linear-gradient(135deg,#f2efe9 0%,#d9c6b8 40%,#5da8d9 70%,#e8edf1 100%)}
.inside-right-curve{position:absolute;top:495px;left:0;width:333px;height:50px}
</style>
</head>
<body>

<section class="stage">
  <article class="single panel cover">
    <div class="brand"><span class="brand-square"></span><span class="brand-name">Crestline<br>Staffing Services</span></div>
    <div class="photo" role="img" aria-label="Photo of a smiling nurse in blue scrubs holding a clipboard"></div>
    <svg class="cover-band" viewBox="0 0 334 393" aria-hidden="true">
      <polygon points="0,100 334,20 334,34 0,114" fill="var(--green)"/>
      <polygon points="0,114 334,34 334,393 0,393" fill="var(--navy)"/>
    </svg>
    <div class="cover-copy">
      <p class="heading cover-kicker">Crestline Staffing Medical</p>
      <p class="cover-title">Providing high<br>quality healthcare<br>professionals</p>
    </div>
    <div class="footer-bar">www.crestlinestaffing.com</div>
  </article>
</section>

<section class="stage">
  <div class="spread">
    <article class="panel flap">
      <div class="photo" role="img" aria-label="Photo of a medical professional consulting with a patient"></div>
      <div class="flap-body">
        <h2 class="heading flap-heading">Our medical staffing specialist will provide you quality employees</h2>
        <p class="flap-text">Searching for skilled staff? Crestline places trusted medical professionals who fit your team, your schedule and your patients, so your facility can stay focused on care every single day.</p>
        <h3 class="heading flap-sub">Crestline Staffing Services can help you</h3>
        <ul class="tick-list">
          <li><svg class="tick" viewBox="0 0 12 12"><circle cx="6" cy="6" r="5.5" fill="var(--green)"/><path d="M3.3 6.2l1.8 1.8 3.6-3.6" stroke="#fff" stroke-width="1.4" fill="none"/></svg>Reduce your overtime and turnover costs</li>
          <li><svg class="tick" viewBox="0 0 12 12"><circle cx="6" cy="6" r="5.5" fill="var(--green)"/><path d="M3.3 6.2l1.8 1.8 3.6-3.6" stroke="#fff" stroke-width="1.4" fill="none"/></svg>Operate more efficiently</li>
          <li><svg class="tick" viewBox="0 0 12 12"><circle cx="6" cy="6" r="5.5" fill="var(--green)"/><path d="M3.3 6.2l1.8 1.8 3.6-3.6" stroke="#fff" stroke-width="1.4" fill="none"/></svg>Add flexibility to your workforce</li>
          <li><svg class="tick" viewBox="0 0 12 12"><circle cx="6" cy="6" r="5.5" fill="var(--green)"/><path d="M3.3 6.2l1.8 1.8 3.6-3.6" stroke="#fff" stroke-width="1.4" fill="none"/></svg>Adapt to changing demands</li>
        </ul>
      </div>
      <div class="footer-bar">www.crestlinestaffing.com</div>
    </article>

    <article class="panel back">
      <div class="back-mark"></div>
      <div class="back-body">
        <p class="heading back-kicker">Crestline Staffing Medical</p>
        <p class="back-text">Need general labor staffing, administrative staffing and manufacturing staffing throughout Indiana, Illinois, and Kentucky? Get in touch.</p>
        <p class="heading contact-title">Contact Us</p>
        <div class="contact-rule"></div>
        <p class="contact-lines">418 Harbor View Rd.<br>Lakeside, Indiana 47000<br>555-014-2290<br>crestlinestaffing.com</p>
        <div class="social"><span></span><span></span><span></span><span></span></div>
      </div>
      <svg class="back-wave" viewBox="0 0 334 220" aria-hidden="true">
        <path d="M0 40 C110 0 220 90 334 50 L334 220 L0 220 Z" fill="var(--sky)"/>
        <path d="M0 90 C120 60 220 130 334 100 L334 220 L0 220 Z" fill="var(--sky-soft)" opacity=".45"/>
      </svg>
      <div class="footer-bar">www.crestlinestaffing.com</div>
    </article>

    <article class="panel cover">
      <div class="brand"><span class="brand-square"></span><span class="brand-name">Crestline<br>Staffing Services</span></div>
      <div class="photo" role="img" aria-label="Photo of a smiling nurse in blue scrubs holding a clipboard"></div>
      <svg class="cover-band" viewBox="0 0 334 393" aria-hidden="true">
        <polygon points="0,100 334,20 334,34 0,114" fill="var(--green)"/>
        <polygon points="0,114 334,34 334,393 0,393" fill="var(--navy)"/>
      </svg>
      <div class="cover-copy">
        <p class="heading cover-kicker">Crestline Staffing Medical</p>
        <p class="cover-title">Providing high<br>quality healthcare<br>professionals</p>
      </div>
      <div class="footer-bar">www.crestlinestaffing.com</div>
    </article>
  </div>
</section>

<section class="stage">
  <div class="spread" style="position:relative">
    <article class="panel inside-left">
      <div class="team-photo" role="img" aria-label="Photo of a group of doctors and nurses in white coats and scrubs"></div>
      <svg class="inside-left-curve" viewBox="0 0 334 60" aria-hidden="true"><path d="M0 30 C120 0 230 10 334 20 L334 60 L0 60 Z" fill="var(--panel-grey)"/></svg>
      <div class="about">
        <h2 class="heading about-heading">Who we are</h2>
        <div class="about-rule"></div>
        <p class="about-text">Crestline Staffing is the largest locally owned recruiting company in the Tri-State. We believe strong partnerships are the foundation of our success. We provide customized staffing solutions for many industries, including medical.</p>
        <p class="heading about-pledge">Put your trust in us, and<br>we will take care of<br>your medical staffing needs.</p>
      </div>
      <div class="footer-bar">www.crestlinestaffing.com</div>
    </article>

    <article class="panel inside-mid">
      <svg class="inside-mid-curve" viewBox="0 0 333 60" aria-hidden="true"><path d="M0 20 C110 30 230 5 333 25 L333 60 L0 60 Z" fill="#fff"/></svg>
      <ul class="services">
        <li class="service">
          <span class="service-icon"><svg width="22" height="22" viewBox="0 0 22 22"><circle cx="11" cy="11" r="8" fill="none" stroke="var(--sky)" stroke-width="2"/><path d="M11 6v5l3 2" stroke="var(--sky)" stroke-width="2" fill="none"/></svg></span>
          <div><h3 class="heading service-title">Temporary Staffing</h3><p class="service-text">Never worry about having the right number of workers on hand. Our flexible team fills short gaps quickly, so your shifts stay covered without any added stress.</p></div>
        </li>
        <li class="service">
          <span class="service-icon"><svg width="22" height="22" viewBox="0 0 22 22"><rect x="5" y="3" width="12" height="16" rx="1" fill="none" stroke="var(--sky)" stroke-width="2"/><path d="M8 8h6M8 12h6" stroke="var(--sky)" stroke-width="2"/></svg></span>
          <div><h3 class="heading service-title">Temp-to-Hire</h3><p class="service-text">Try before you commit. Evaluate each candidate on the job first, then bring the right person onto your permanent team with full confidence.</p></div>
        </li>
        <li class="service">
          <span class="service-icon"><svg width="22" height="22" viewBox="0 0 22 22"><circle cx="11" cy="7" r="4" fill="none" stroke="var(--sky)" stroke-width="2"/><path d="M4 19c1-4 4-6 7-6s6 2 7 6" stroke="var(--sky)" stroke-width="2" fill="none"/></svg></span>
          <div><h3 class="heading service-title">Direct Hire</h3><p class="service-text">We search, screen and interview so you meet only qualified candidates, saving your managers valuable time in the hiring process.</p></div>
        </li>
        <li class="service">
          <span class="service-icon"><svg width="22" height="22" viewBox="0 0 22 22"><rect x="3" y="6" width="16" height="11" rx="1" fill="none" stroke="var(--sky)" stroke-width="2"/><circle cx="11" cy="11.5" r="2.5" fill="var(--sky)"/></svg></span>
          <div><h3 class="heading service-title">Payrolling</h3><p class="service-text">Give us the employees you recruit and we handle payroll, taxes and paperwork, keeping your records simple and accurate.</p></div>
        </li>
      </ul>
      <div class="footer-bar">www.crestlinestaffing.com</div>
    </article>

    <article class="panel inside-right">
      <div class="offer">
        <h2 class="heading offer-heading">Our Services</h2>
        <div class="offer-rule"></div>
        <p class="offer-group">Administrative</p>
        <ul class="offer-list">
          <li><svg class="tick" viewBox="0 0 12 12"><circle cx="6" cy="6" r="5.5" fill="var(--green)"/><path d="M3.3 6.2l1.8 1.8 3.6-3.6" stroke="#fff" stroke-width="1.4" fill="none"/></svg>Billing Specialists</li>
          <li><svg class="tick" viewBox="0 0 12 12"><circle cx="6" cy="6" r="5.5" fill="var(--green)"/><path d="M3.3 6.2l1.8 1.8 3.6-3.6" stroke="#fff" stroke-width="1.4" fill="none"/></svg>Coding Specialists</li>
          <li><svg class="tick" viewBox="0 0 12 12"><circle cx="6" cy="6" r="5.5" fill="var(--green)"/><path d="M3.3 6.2l1.8 1.8 3.6-3.6" stroke="#fff" stroke-width="1.4" fill="none"/></svg>Medical Records</li>
          <li><svg class="tick" viewBox="0 0 12 12"><circle cx="6" cy="6" r="5.5" fill="var(--green)"/><path d="M3.3 6.2l1.8 1.8 3.6-3.6" stroke="#fff" stroke-width="1.4" fill="none"/></svg>Office Managers</li>
          <li><svg class="tick" viewBox="0 0 12 12"><circle cx="6" cy="6" r="5.5" fill="var(--green)"/><path d="M3.3 6.2l1.8 1.8 3.6-3.6" stroke="#fff" stroke-width="1.4" fill="none"/></svg>Receptionists</li>
        </ul>
        <p class="offer-group">Clinical</p>
        <ul class="offer-list">
          <li><svg class="tick" viewBox="0 0 12 12"><circle cx="6" cy="6" r="5.5" fill="var(--green)"/><path d="M3.3 6.2l1.8 1.8 3.6-3.6" stroke="#fff" stroke-width="1.4" fill="none"/></svg>Certified Medical Assistants</li>
          <li><svg class="tick" viewBox="0 0 12 12"><circle cx="6" cy="6" r="5.5" fill="var(--green)"/><path d="M3.3 6.2l1.8 1.8 3.6-3.6" stroke="#fff" stroke-width="1.4" fill="none"/></svg>Registered Medical Assistants</li>
          <li><svg class="tick" viewBox="0 0 12 12"><circle cx="6" cy="6" r="5.5" fill="var(--green)"/><path d="M3.3 6.2l1.8 1.8 3.6-3.6" stroke="#fff" stroke-width="1.4" fill="none"/></svg>Certified Nursing Assistants</li>
          <li><svg class="tick" viewBox="0 0 12 12"><circle cx="6" cy="6" r="5.5" fill="var(--green)"/><path d="M3.3 6.2l1.8 1.8 3.6-3.6" stroke="#fff" stroke-width="1.4" fill="none"/></svg>Phlebotomists</li>
        </ul>
      </div>
      <div class="photo" role="img" aria-label="Photo of a young doctor caring for an elderly patient"></div>
      <svg class="inside-right-curve" viewBox="0 0 333 50" aria-hidden="true"><path d="M0 25 C110 45 220 5 333 30 L333 0 L0 0 Z" fill="var(--navy-deep)"/><path d="M0 25 C110 45 220 5 333 30" stroke="var(--sky)" stroke-width="4" fill="none"/></svg>
      <div class="footer-bar">www.crestlinestaffing.com</div>
    </article>
  </div>
</section>

</body>
</html>
```